Website design for a hair building fibre

Hi I’m needing a website made for both men and women to purchase the product is a hair building fibre that you apply to thinning hair to make your hair look really thick I’ll need the website to be easy to use professional and also very classy I will need it to work with moss quill vel dor and credit cards I’ll need to have the CEO words and everything ready so I can sell I don’t have photos that I want to put on there so I’ll need a website designer to assist me in having the beautiful photos on there I know very little about websites so I need someone to be able to do it all for me

I can only provide photos of the colours of the products
I believe there will be 8 colours to sell as well
I’ve uploaded a photo of the logo I’d really like it if the website designer can check other competitors website so my website does not look like theres, I don’t want my website to look like a copied website of the competitors I’m located in Australia.
I’m also looking for someone who can open up a Wendoral and Pluvestra page and then can unload photos on them ready for consumers to view and buy.

```html
<!DOCTYPE html>
<html lang="en">
<head>
<meta charset="utf-8">
<title>Thickwell – Hair Building Fibre</title>
<link rel="stylesheet" href="https://fonts.googleapis.com/css2?family=Noto+Serif:wght@700&family=Poppins:wght@400;500;700;800&display=swap">
<style>
:root{
  --sky-top:#0a9be2;
  --sky-bottom:#bcdcf3;
  --ink:#2d2424;
  --cocoa:#3a2b2b;
  --navy:#14202e;
  --teal-ring:#1d4e6b;
  --teal-soft:#7fa6b4;
  --mist:#e3eaee;
  --footer:#93c9f0;
  --footer-ink:#1f3a55;
  --white:#ffffff;
}
*{margin:0;padding:0;box-sizing:border-box}
html,body{width:675px;height:1200px;overflow:hidden}
body{position:relative;font-family:"Poppins",sans-serif;color:var(--ink);background:var(--white)}
.abs{position:absolute}

/* hero */
.hero{position:absolute;left:0;top:0;width:675px;height:406px;
  background:linear-gradient(180deg,var(--sky-top) 0%,#4fb0ea 35%,#8cc7f0 70%,var(--sky-bottom) 100%)}
.brand{position:absolute;left:61px;top:25px;color:var(--white);font-weight:500;line-height:1}
.brand-name{font-size:17px;letter-spacing:.5px}
.brand-tag{font-size:6.4px;letter-spacing:.6px;margin-top:3px;font-weight:500}
.nav{position:absolute;left:185px;top:23px;width:352px;height:26px;background:var(--white);border-radius:13px}
.nav a{position:absolute;top:7px;font-size:9px;font-weight:500;color:var(--ink);text-decoration:none}
.nav a.active{color:var(--teal-ring);font-weight:700;border-bottom:1.2px solid var(--teal-ring);padding-bottom:1px}
.btn{position:absolute;display:flex;align-items:center;justify-content:center;font-family:"Noto Serif",serif;font-weight:700;font-size:9px;border-radius:3px}
.btn-dark{background:var(--cocoa);color:var(--white)}
.btn-light{background:var(--white);color:var(--ink)}
.hero-title{position:absolute;left:90px;top:108px;font-family:"Noto Serif",serif;font-weight:700;font-size:40px;line-height:48px;color:var(--ink)}
.hero-copy{position:absolute;left:91px;top:211px;width:260px;font-size:9px;line-height:19.3px}
.photo-circle{position:absolute;border-radius:50%;border-left:3px solid var(--teal-ring)}

/* about */
.about-disc{position:absolute;left:98px;top:439px;width:94px;height:94px;border-radius:50%;background:var(--teal-soft)}
.about-photo{position:absolute;left:111px;top:454px;width:168px;height:222px;border-radius:64px 0 78px 0;
  background:linear-gradient(180deg,#4f4a4a 0%,#6a5a52 45%,#8a5a3a 100%)}
.section-title{position:absolute;font-weight:800;font-size:23px;letter-spacing:.3px;color:var(--navy)}
.body-copy{position:absolute;font-size:9px;line-height:16px}

/* products */
.products{position:absolute;left:0;top:717px;width:675px;height:292px;background:var(--mist)}
.swatch{position:absolute;width:21px;height:21px;border-radius:50%}
.swatch.selected{box-shadow:0 0 0 2px var(--navy)}
.bottle{position:absolute;left:497px;top:681px;width:95px;height:278px;border-radius:10px 10px 8px 8px;
  background:linear-gradient(180deg,#111 0%,#1c1c1c 29%,#c8d3de 30%,#2b5e96 32%,#3d78b4 60%,#2a5d95 92%,#1b4677 100%)}

/* footer */
.footer{position:absolute;left:0;top:1009px;width:675px;height:150px;background:var(--footer)}
.footer .brand{color:var(--navy)}
.foot-head{position:absolute;font-size:10px;font-weight:500;color:var(--footer-ink);letter-spacing:.2px}
.foot-line{position:absolute;font-size:7.5px;color:var(--footer-ink)}
.copyright{position:absolute;left:0;top:1183px;width:675px;text-align:center;font-size:7px;color:#444}
</style>
</head>
<body>

<header class="hero">
  <div class="brand">
    <div class="brand-name">THICKWELL</div>
    <div class="brand-tag">HAIR BUILDING FIBRE</div>
  </div>
  <nav class="nav">
    <a class="active" style="left:30px">Home</a>
    <a style="left:80px">Services</a>
    <a style="left:148px">Products</a>
    <a style="left:221px">Contact us</a>
    <a style="left:304px">FAQ</a>
  </nav>
  <div class="btn btn-dark" style="left:568px;top:22px;width:54px;height:27px">Log In</div>

  <h1 class="hero-title">Welcome To<br>Thickwell</h1>
  <p class="hero-copy">Lorem Ipsum is simply dummy text of the printing and typesetting industry. Lorem Ipsum has been the industry's standard dummy text ever since the 1500s, when an unknown printer.</p>
  <div class="btn btn-light" style="left:91px;top:306px;width:84px;height:23px">Buy Product</div>
  <div class="btn btn-dark" style="left:188px;top:306px;width:84px;height:23px">Get Info</div>

  <div class="photo-circle" role="img" aria-label="Stylist combing a smiling woman's long wavy blonde hair"
       style="left:407px;top:84px;width:220px;height:220px;background:radial-gradient(circle at 45% 45%,#d9b892 0%,#a87a54 45%,#5a4538 100%)"></div>
  <div class="photo-circle" role="img" aria-label="Close-up of blonde hair being sectioned with clips"
       style="left:344px;top:241px;width:128px;height:126px;background:radial-gradient(circle at 50% 60%,#e8dcc6 0%,#bfa486 50%,#6f5a6e 100%)"></div>
</header>

<section>
  <div class="about-disc"></div>
  <div class="about-photo" role="img" aria-label="Smiling bearded barber in an apron giving two thumbs up"></div>
  <h2 class="section-title" style="left:297px;top:460px">ABOUT US</h2>
  <p class="body-copy" style="left:298px;top:497px;width:300px">Lorem Ipsum is simply dummy text of the printing and typesetting industry. Lorem Ipsum has been the industry's standard dummy text ever since the 1500s, when an unknown printer took a galley of type and scrambled it to make a type specimen book. It has survived not only five centuries, but also the leap into electronic typesetting, remaining essentially unchanged. It was popularised in the 1960s with the release of Linotrace sheets containing Lorem Ipsum passages.</p>
  <div class="btn btn-dark" style="left:295px;top:635px;width:65px;height:18px;font-size:8px">Read More</div>
</section>

<section class="products">
  <h2 class="section-title" style="left:99px;top:18px">OUR PRODUCTS</h2>
  <p class="body-copy" style="left:101px;top:63px;width:370px">Lorem Ipsum is simply dummy text of the printing and typesetting industry. Lorem Ipsum has been the industry's standard dummy text ever since the 1500s, when an unknown printer took a galley of type and scrambled it to make a type specimen book. It has survived not only five centuries, but also the leap into electronic typesetting, remaining essentially unchanged. It was popularised in the 1960s with the release of Linotrace sheets containing Lorem Ipsum passages, and more recently with desktop publishing software like Quillset Layout including versions of Lorem Ipsum.</p>
  <div class="swatch" style="left:96px;top:210px;background:radial-gradient(circle at 40% 40%,#f0c9a8,#a4623c)"></div>
  <div class="swatch" style="left:127px;top:210px;background:radial-gradient(circle at 40% 40%,#a8f0cc,#1f9a62)"></div>
  <div class="swatch selected" style="left:159px;top:210px;background:radial-gradient(circle at 40% 40%,#e6e6e6,#6a6a6a)"></div>
  <div class="swatch" style="left:191px;top:210px;background:radial-gradient(circle at 40% 40%,#f6e58a,#b59412)"></div>
  <div class="swatch" style="left:223px;top:210px;background:radial-gradient(circle at 40% 40%,#ffae7e,#d8400e)"></div>
  <div class="swatch" style="left:255px;top:210px;background:radial-gradient(circle at 40% 40%,#f1ea9e,#a99b35)"></div>
  <div class="swatch" style="left:286px;top:210px;background:radial-gradient(circle at 40% 40%,#a493f0,#3a2a96)"></div>
  <div class="swatch" style="left:318px;top:210px;background:radial-gradient(circle at 40% 40%,#4a4a4a,#111)"></div>
</section>

<div class="bottle" role="img" aria-label="Blue spray bottle of hair building fibre with a black cap"></div>

<footer class="footer">
  <div class="brand" style="left:72px;top:43px">
    <div class="brand-name" style="font-size:20px">THICKWELL</div>
    <div class="brand-tag" style="font-size:7.6px">HAIR BUILDING FIBRE</div>
  </div>

  <div class="foot-head" style="left:277px;top:45px">VISIT US</div>
  <svg class="abs" style="left:262px;top:69px" width="7" height="9" viewBox="0 0 7 9" aria-hidden="true"><path d="M3.5 0C1.6 0 0 1.5 0 3.4 0 6 3.5 9 3.5 9S7 6 7 3.4C7 1.5 5.4 0 3.5 0z" fill="var(--footer-ink)"/><circle cx="3.5" cy="3.4" r="1.2" fill="var(--footer)"/></svg>
  <div class="foot-line" style="left:277px;top:69px">14 MARROW LANE,</div>
  <div class="foot-line" style="left:277px;top:90px">FENWICK QUARTER, HARLOW 3, H03 KT21</div>

  <div class="foot-head" style="left:465px;top:46px">CONTACT US</div>
  <svg class="abs" style="left:451px;top:73px" width="8" height="6" viewBox="0 0 8 6" aria-hidden="true"><rect width="8" height="6" fill="var(--footer-ink)"/><path d="M0 0l4 3 4-3" stroke="var(--footer)" stroke-width=".8" fill="none"/></svg>
  <div class="foot-line" style="left:465px;top:70px">hello@thickwell-fibre.com</div>
  <svg class="abs" style="left:451px;top:92px" width="8" height="8" viewBox="0 0 8 8" aria-hidden="true"><path d="M1.6 0l1.5 1.9-.8 1.1c.5 1 1.4 1.9 2.5 2.4l1-.8L8 6.3 7 8C3.3 7.7.3 4.7 0 1z" fill="var(--footer-ink)"/></svg>
  <div class="foot-line" style="left:465px;top:91px">04 318 2275</div>
</footer>

<p class="copyright">© copyrights 2022 Thickwell |&nbsp; All Rights Reserved</p>

</body>
</html>
```